Medical Skincare services/menu/pricing Booklet 12 pages

We need produce a 12-page glossy, saddle-stitched booklet (5 1/2" tall X 81/2" wide). The booklet will be used as a services menu for a skin care salon. I have mocked up the booklet (w/ all copy) in WORD and I've provided a separate PDF of the accurate page order (see files attached). IMPORTANT: Feel free to use your creativity yet style-wise it should kinda match my wife's website colors and text style. Her clients are demanding so she wants a clean, high end, modern look (ala Apple maybe?). See her website for a frame of reference www.GlowWithMara.example
Updates

Target Market(s)

upscale female, professional women, teens with acne

Industry/Entity Type

Medical

Requirements
Must have
• the pics in the mock up are important. I've attached them here

```html
<!DOCTYPE html>
<html lang="en">
<head>
<meta charset="utf-8">
<title>Mara Ellison – About &amp; Testimonials Spread</title>
<link href="https://fonts.googleapis.com/css2?family=Mulish:ital,wght@0,300;0,400;0,500;1,300;1,400&display=swap" rel="stylesheet">
<style>
  :root{
    --slate:#5f5e70;
    --tan:#a89b82;
    --tan-dark:#8f8268;
    --gold:#c2ad86;
    --paper:#ffffff;
    --ink:#2b2b2b;
    --muted:#9a9a9a;
    --rule:#b8ad98;
    --soft:#e9e7ee;
  }
  *{margin:0;padding:0;box-sizing:border-box}
  html,body{width:1200px;height:423px;overflow:hidden;background:#fff}
  body{font-family:"Mulish",Helvetica,Arial,sans-serif;position:relative}
  .spread{position:relative;width:1200px;height:423px}
  .page{position:absolute;top:0;height:423px}
  .page-left{left:0;width:617px;background:var(--slate)}
  .page-right{left:619px;width:581px;background:var(--paper)}
  .hero-photo{position:absolute;left:0;top:0;width:282px;height:423px;
    background:linear-gradient(100deg,#d9d2c2 0%,#b9b1a0 30%,#7e9a96 55%,#5d7770 75%,#c4bba8 100%)}
  .owner-name{position:absolute;left:303px;top:36px;font-size:16px;font-weight:500;color:var(--gold)}
  .owner-title{position:absolute;left:303px;top:57px;font-size:8px;font-weight:300;color:#b4a88f}
  .owner-bio{position:absolute;left:303px;top:79px;width:293px;font-size:9.6px;line-height:14.6px;font-weight:300;color:var(--soft);text-align:justify}
  .promise-box{position:absolute;left:222px;top:234px;width:333px;height:135px;background:var(--tan);padding:16px 15px 0 15px}
  .promise-title{font-size:10.5px;font-style:italic;font-weight:400;color:#fff;margin-bottom:6px}
  .promise-text{font-size:7.6px;line-height:11.2px;font-weight:300;color:#f4f0e8;text-align:justify}
  .signature{position:absolute;left:235px;top:102px;width:95px;height:22px;background:linear-gradient(90deg,rgba(255,255,255,.15),rgba(255,255,255,.35))}
  .rule-left{position:absolute;left:0;top:386px;width:617px;height:1px;background:#e8e4dc}
  .page-num{position:absolute;width:16px;height:16px;background:var(--slate);color:#fff;font-size:8px;text-align:center;line-height:16px}
  .page-num.left{left:38px;top:396px;background:#56556a;border-bottom:1px solid #fff}
  .page-num.right{left:527px;top:398px}
  .section-band{position:absolute;left:0;top:0;width:47px;height:423px;background:var(--tan)}
  .section-title{position:absolute;left:24px;top:150px;transform:translate(-50%,-50%) rotate(-90deg);font-size:33px;font-weight:300;color:#fff;white-space:nowrap;letter-spacing:.5px}
  .rule-right{position:absolute;left:47px;top:386px;width:510px;height:1px;background:var(--rule)}
  .testimonial{position:absolute;width:220px;height:100px}
  .client-photo{position:absolute;left:0;top:0;width:78px;height:78px}
  .client-quote{position:absolute;left:83px;top:0;width:135px;font-size:7.5px;line-height:9.7px;font-style:italic;font-weight:400;color:var(--ink);text-align:justify;padding-bottom:4px;border-bottom:1px solid #555}
  .client-name{position:absolute;left:0;top:84px;font-size:8px;font-weight:400;color:#8a8a8a;letter-spacing:.3px;white-space:nowrap}
  .client-role{position:absolute;left:0;top:95px;font-size:6px;color:#b0b0b0;white-space:nowrap}
</style>
</head>
<body>
<div class="spread">
  <section class="page page-left">
    <div class="hero-photo" role="img" aria-label="Portrait of the owner in a long patterned dress leaning against a stone column beside flower pots"></div>
    <h1 class="owner-name">Mara Ellison</h1>
    <p class="owner-title">Medical Aesthetician &amp; Owner</p>
    <p class="owner-bio">As a teenager, I had cystic acne so bad that I would ditch school to swim in the ocean because the salt water seemed to dry out and heal my skin. I was on such a mission to clear my skin that I spent my weekly allowance on skin care products I saw on TV. Then, I memorized every ingredient. I was so intrigued by the beauty industry that, by 19, I began a career as a make up artist for Lumera, Maven, Bonny Bree, Presca, and Stello. By 23, I was a skincare consultant for the Giselle Klein Salons in Beverly Hills and Orange County California. I was honored to learn from the world's most demanding clients.</p>
    <div class="promise-box">
      <h2 class="promise-title">I Understand Why Your Skin Matters</h2>
      <p class="promise-text">Admit it. We take more pictures of ourselves than ever...and then try to "fix" our blemishes with photo filters. I understand your frustrations. Some of you know I've had a parallel career as a professional singer with dozens of network TV appearances, where the HD cameras take extreme close ups...Yikes!). I also sing the National Anthem at national league games, where their 200 foot-wide arena screens constantly remind me that skin imperfections are magnified. I will help get your skin more naturally beautiful so you can use less photo filters :-)</p>
      <div class="signature" role="img" aria-label="Handwritten signature of Mara Ellison"></div>
    </div>
    <div class="rule-left"></div>
    <div class="page-num left">2</div>
  </section>

  <section class="page page-right">
    <div class="section-band"><h2 class="section-title">Testimonials</h2></div>

    <article class="testimonial" style="left:335px;top:35px">
      <div class="client-photo" role="img" aria-label="Portrait photo of client" style="background:linear-gradient(160deg,#c9b9a8,#6b4a3a)"></div>
      <p class="client-quote">Having ethnic skin I've been hesitant about having treatments but Mara immediately put me at ease. She has taught me so much about my skin and how to care for it. Each time I've left with my skin looking and feeling amazing.</p>
      <p class="client-name">DALIA HARTWELL</p>
      <p class="client-role">Real Estate Agent</p>
    </article>

    <article class="testimonial" style="left:76px;top:150px">
      <div class="client-photo" role="img" aria-label="Portrait photo of client" style="background:linear-gradient(160deg,#f1ece4,#d9c08e)"></div>
      <p class="client-quote" style="top:54px">Mara is someone I definitely trust with my skincare needs because she truly cares about people and their issues.</p>
      <p class="client-name">TESSA ROWAN</p>
      <p class="client-role">Reality TV Star/Coastal Wives of Orange County</p>
    </article>

    <article class="testimonial" style="left:335px;top:150px">
      <div class="client-photo" role="img" aria-label="Portrait photo of client" style="background:linear-gradient(160deg,#f4e6dc,#e2b98c)"></div>
      <p class="client-quote">I have now had two facials by Mara and each time my skin feels so refreshed and new! She has also helped my teenage son who has acne. Mara knew exactly what he needed and is already getting clearer skin. Worth every penny.</p>
      <p class="client-name">KIRA MADDOX</p>
      <p class="client-role">Mother of Five</p>
    </article>

    <article class="testimonial" style="left:76px;top:273px">
      <div class="client-photo" role="img" aria-label="Portrait photo of client" style="background:linear-gradient(160deg,#8a7c6c,#7a4a35)"></div>
      <p class="client-quote">I have been seeing Mara Ellison for HydraGlow facials. Ever since my first HydraGlow my skin has had a healthy glow and texture. As an Aesthetic Professional, she helps me feel my personal best.</p>
      <p class="client-name">CAROL NYBERG</p>
      <p class="client-role">R.N.</p>
    </article>

    <article class="testimonial" style="left:335px;top:273px">
      <div class="client-photo" role="img" aria-label="Portrait photo of client" style="background:linear-gradient(160deg,#a88a6e,#d8b59a)"></div>
      <p class="client-quote">I've been seeing Mara on a regular basis because she always goes above and beyond to ensure that I'm comfortable. She made the experience all about me and my skincare needs. She is highly knowledgable and offers creative options to make sure I get what I need.</p>
      <p class="client-name">ELISE STANFORD</p>
      <p class="client-role">Marketing Exec.</p>
    </article>

    <div class="rule-right"></div>
    <div class="page-num right">3</div>
  </section>
</div>
</body>
</html>
```